BRCW Business Cards

Business Cards should contain:
Bright Ridgecrest Coating Works
Felix Darrow
M: 0417 865 093
E: brightRCW@fernpost.example
BRCW logo
TCG logo
Painting & Decorating
Licence # 719362K
slogan: feel the mark of modern perfection

Target Market(s)

all aspect of painting

Industry/Entity Type

Trade

Contact Information for Business Card

Felix Darrow
M: 0417 865 093
E: brightRCW@fernpost.example
BRCW logo
TCG logo
Painting & Decorating
Licence # 719362K

Font styles to use
Serif
Sans Serif

Requirements
Must have
• clear design with nice backround
• two sides
• smal TCG logo
Nice to have
• easy to read
Should not have
• mess
• black
• plastics form

```html
<!DOCTYPE html>
<html lang="en">
<head>
<meta charset="utf-8">
<title>BRCW Business Cards</title>
<link rel="stylesheet" href="https://fonts.googleapis.com/css2?family=Open+Sans:wght@400;600;700&family=PT+Serif:wght@700&display=swap">
<style>
  :root {
    --stage: #2e2f30;
    --card-white: #ffffff;
    --card-dark-top: #1d201e;
    --card-dark-bottom: #0b0c0b;
    --brand-green: #4d8a57;
    --logo-green: #1f4a3a;
    --ink-teal: #2f5853;
    --rule-grey: #8f8f8f;
    --badge-blue: #3f6fae;
  }
  * { box-sizing: border-box; margin: 0; padding: 0; }
  html, body { width: 1200px; height: 885px; overflow: hidden; }
  body {
    background: var(--stage);
    display: flex;
    flex-direction: column;
    align-items: center;
    justify-content: center;
    gap: 40px;
    font-family: "Open Sans", Arial, sans-serif;
  }
  .card {
    position: relative;
    width: 640px;
    height: 390px;
    border-radius: 4px;
    overflow: hidden;
  }
  /* Back side */
  .card-back {
    background: linear-gradient(160deg, var(--card-dark-top), var(--card-dark-bottom));
    display: flex;
    align-items: center;
    justify-content: center;
  }
  .service-line {
    color: var(--brand-green);
    font-size: 34px;
    font-weight: 600;
    letter-spacing: 0.5px;
  }
  /* Front side */
  .card-front { background: var(--card-white); }
  .brand {
    position: absolute;
    left: 34px;
    top: 92px;
    display: flex;
    align-items: center;
    gap: 14px;
  }
  .brand-mark {
    width: 46px;
    height: 46px;
    background: var(--brand-green);
    border-radius: 4px;
  }
  .brand-words {
    border-left: 1.5px solid var(--logo-green);
    padding-left: 10px;
    font-family: "PT Serif", Georgia, serif;
    font-weight: 700;
    color: var(--logo-green);
  }
  .brand-initials { font-size: 34px; line-height: 1.05; }
  .brand-name { font-size: 13px; line-height: 1.25; max-width: 150px; }
  .holder {
    position: absolute;
    right: 30px;
    top: 108px;
    text-align: right;
  }
  .holder-name {
    color: var(--brand-green);
    font-size: 22px;
    font-weight: 700;
  }
  .holder-rule {
    position: absolute;
    left: 330px;
    right: 0;
    top: 144px;
    border-top: 1.5px solid var(--rule-grey);
  }
  .tagline {
    position: absolute;
    right: 30px;
    top: 152px;
    color: var(--ink-teal);
    font-size: 15px;
  }
  .association-badge {
    position: absolute;
    right: 40px;
    top: 184px;
    width: 48px;
    height: 44px;
    border-radius: 4px;
    background: var(--badge-blue);
  }
  .section-rule {
    position: absolute;
    left: 0;
    right: 0;
    top: 250px;
    border-top: 1.5px solid var(--rule-grey);
  }
  .contact {
    position: absolute;
    left: 42px;
    top: 272px;
    color: var(--ink-teal);
    font-size: 17px;
    line-height: 26px;
    list-style: none;
  }
  .contact li { display: flex; align-items: center; gap: 12px; }
  .contact .licence { padding-left: 26px; }
  .contact svg { width: 14px; height: 14px; fill: var(--ink-teal); flex: none; }
</style>
</head>
<body>
  <section class="card card-back">
    <p class="service-line">Painting &amp; Decorating</p>
  </section>

  <section class="card card-front">
    <div class="brand">
      <span class="brand-mark"></span>
      <div class="brand-words">
        <div class="brand-initials">BRCW</div>
        <div class="brand-name">Bright Ridgecrest Coating Works</div>
      </div>
    </div>

    <div class="holder"><p class="holder-name">Felix Darrow</p></div>
    <div class="holder-rule"></div>
    <p class="tagline">Feel the mark of modern perfection</p>
    <div class="association-badge"></div>

    <div class="section-rule"></div>

    <ul class="contact">
      <li class="licence">Licence # 719362K</li>
      <li>
        <svg viewBox="0 0 24 24" aria-hidden="true"><path d="M6.6 10.8a15.1 15.1 0 0 0 6.6 6.6l2.2-2.2c.3-.3.7-.4 1-.2 1.1.4 2.3.6 3.6.6.6 0 1 .4 1 1V20c0 .6-.4 1-1 1A17 17 0 0 1 3 4c0-.6.4-1 1-1h3.5c.6 0 1 .4 1 1 0 1.3.2 2.5.6 3.6.1.3 0 .7-.2 1z"/></svg>
        0417 865 093
      </li>
      <li>
        <svg viewBox="0 0 24 24" aria-hidden="true"><path d="M2 5h20v14H2z M3 6l9 7 9-7" fill="var(--ink-teal)"/></svg>
        brightRCW@fernpost.example
      </li>
    </ul>
  </section>
</body>
</html>
```